Website - Tides Of Bloom

We are catalysts of change in people's lives.
We work with individuals and professionals to bring about instant substantial & transforming change in their lives.
We provide one-on-one lifestyle coaching by an experienced practitioner.
Our existing website is www.tidesofbloom.biz & this site contains our the basis for the content of our desired new project, so please examine this carefully.
We require a professional and captivating website that will instantly impress, engage invite our readers to click & invest their lives.
Our services do not come cheap, but are second to none.
Our website must be contemporary whilst reflecting indisputable class & ultra-confidence in the success of our work.
Target Market(s)
Those who seek to want to change in their lives. Those aged primarily between 30 and 50 years of age, male or female.
Industry/Entity Type
Work
Look and feel

```html
<!DOCTYPE html>
<html lang="en">
<head>
<meta charset="utf-8">
<title>Tides Of Bloom</title>
<link rel="stylesheet" href="https://fonts.googleapis.com/css2?family=Roboto+Condensed:wght@400;700&display=swap">
<style>
:root{
  --bg:#000;
  --ink:#fff;
  --dark:#1a1a1a;
  --orange:#e8572a;
  --green:#a6c23a;
  --teal:#2b8ab0;
  --stripe-green:#2e8b3c;
  --card-top:#ececec;
  --footer:#262626;
}
*{margin:0;padding:0;box-sizing:border-box}
html,body{width:853px;height:1200px;overflow:hidden;background:var(--bg)}
body{position:relative;font-family:"Roboto Condensed",Arial,sans-serif;color:var(--ink)}
.abs{position:absolute}
.brand{display:flex;align-items:center;gap:8px;font-size:17px;font-weight:700;color:var(--ink);line-height:1}
.brand-mark{width:30px;height:30px;background:var(--orange)}
.nav{top:40px;left:458px;display:flex;gap:0;font-size:12px}
.nav a{color:var(--ink);text-decoration:none;position:absolute;white-space:nowrap}
.nav a.active{color:var(--orange)}
.hero-photo{left:107px;top:59px;width:639px;height:252px;background:linear-gradient(180deg,#6d6577 0%,#b9a79a 35%,#d8c6a6 48%,#8a6f7a 62%,#3f3447 100%)}
.hero-panel{left:430px;top:171px;width:316px;height:120px;background:rgba(0,0,0,.45)}
.hero-line1{left:453px;top:194px;font-size:18px;font-weight:700;white-space:nowrap}
.hero-line1 .accent{color:var(--green)}
.hero-line2{left:514px;top:215px;font-size:18px;font-weight:700;color:var(--teal)}
.cta{left:494px;top:246px;width:195px;height:30px;background:var(--orange);border-radius:6px;font-size:21px;font-weight:700;text-align:center;line-height:30px;color:var(--ink)}
.card{top:326px;width:191px;height:216px;background:#fff;border-radius:5px;overflow:hidden;color:var(--dark)}
.card-head{height:57px;background:var(--card-top);position:relative}
.card-stripe{height:5px;background:linear-gradient(90deg,var(--stripe-green) 0 33%,var(--orange) 33% 66%,var(--teal) 66%)}
.card-icon{position:absolute;left:70px;top:4px;width:50px;height:50px;border-radius:50%;border:2px solid var(--dark);background:#fff;display:flex;align-items:center;justify-content:center}
.card-icon span{width:36px;height:36px;border-radius:50%;background:var(--dark)}
.card-title{text-align:center;font-size:17px;font-weight:700;margin-top:8px}
.card-text{font-size:10px;line-height:12px;text-transform:uppercase;padding:4px 14px 0 18px}
.rule{left:123px;width:622px;height:1px;background:var(--ink)}
.section-title{font-size:17px;font-weight:700;white-space:nowrap}
.story-list{left:123px;top:598px;list-style:none;font-size:10px}
.story-list li{height:17px;line-height:14px;display:flex;gap:6px;align-items:center}
.story-list svg{flex:none}
.laptop-screen{left:516px;top:599px;width:201px;height:131px;background:#111;border-radius:6px 6px 0 0;padding:8px}
.laptop-screen .display{width:100%;height:100%;background:#fff;display:flex;align-items:center;justify-content:center}
.laptop-base{left:482px;top:730px;width:269px;height:12px;background:linear-gradient(#e4e4e4,#9a9a9a);border-radius:0 0 10px 10px}
.photo{position:absolute}
.footer{left:0;top:1102px;width:853px;height:98px;background:var(--footer)}
.call{left:130px;top:1112px;display:flex;align-items:center;gap:10px;font-size:21px;font-weight:700;white-space:nowrap}
.follow{left:539px;top:1110px;font-size:21px;font-weight:700}
.social{top:1106px;width:36px;height:36px;border-radius:50%;background:var(--ink)}
.footer-nav a{position:absolute;top:1152px;font-size:10px;color:var(--ink);text-decoration:none}
.copyright{left:226px;top:1173px;font-size:8px}
</style>
</head>
<body>

<header>
  <div class="abs brand" style="left:127px;top:20px"><span class="brand-mark"></span>Tides of Bloom</div>
  <nav class="abs nav">
    <a class="active" style="left:0">HOME</a>
    <a style="left:54px">BUSINESS</a>
    <a style="left:126px">INDIVIDUAL</a>
    <a style="left:204px">CONTACT</a>
  </nav>
</header>

<section class="hero">
  <div class="abs hero-photo" role="img" aria-label="Runner on a beach at sunset"></div>
  <div class="abs hero-panel"></div>
  <p class="abs hero-line1"><span class="accent">INSTANTLY IMPRESS,</span> ENGAGE READERS</p>
  <p class="abs hero-line2">INVEST THEIR LIVES....</p>
  <a class="abs cta">GET STARTED NOW</a>
</section>

<section class="services">
  <article class="abs card" style="left:126px">
    <div class="card-head"><div class="card-icon"><span role="img" aria-label="Running figure icon"></span></div></div>
    <div class="card-stripe"></div>
    <h3 class="card-title">LIFE SKILLS</h3>
    <p class="card-text">Lorem Ipsum is simply dummy text of the printing and typesetting industry. Lorem Ipsum has been the industry's standard dummy text ever since the 1500s, when an un-known printer took a galley of type and scrambled it to make a type specimen book. It has survived not only five centuries, but also</p>
  </article>
  <article class="abs card" style="left:329px">
    <div class="card-head"><div class="card-icon"><span role="img" aria-label="Group of people icon"></span></div></div>
    <div class="card-stripe"></div>
    <h3 class="card-title">COMMUNICATE</h3>
    <p class="card-text">Lorem Ipsum is simply dummy text of the printing and typesetting industry. Lorem Ipsum has been the industry's standard dummy text ever since the 1500s, when an un-known printer took a galley of type and scrambled it to make a type specimen book. It has survived not only five centuries, but also</p>
  </article>
  <article class="abs card" style="left:534px">
    <div class="card-head"><div class="card-icon"><span role="img" aria-label="Person in speech bubble icon"></span></div></div>
    <div class="card-stripe"></div>
    <h3 class="card-title">MY LIFE</h3>
    <p class="card-text">Lorem Ipsum is simply dummy text of the printing and typesetting industry. Lorem Ipsum has been the industry's standard dummy text ever since the 1500s, when an un-known printer took a galley of type and scrambled it to make a type specimen book. It has survived not only five centuries, but also</p>
  </article>
</section>

<div class="abs rule" style="top:559px"></div>

<section class="story">
  <h2 class="abs section-title" style="left:160px;top:569px">OUR SUCCESS STORY</h2>
  <ul class="abs story-list">
    <li><svg width="10" height="11" viewBox="0 0 10 11"><path d="M0 0H6L10 5.5 6 11H0Z" fill="#fff"/></svg>MORE CHOICES ABOUT YOUR BEHAVIOURS AND EMOTIONS</li>
    <li><svg width="10" height="11" viewBox="0 0 10 11"><path d="M0 0H6L10 5.5 6 11H0Z" fill="#fff"/></svg>IMPROVE YOUR RELATIONSHIPS AND THE WAYS YOU COMMUNICATE</li>
    <li><svg width="10" height="11" viewBox="0 0 10 11"><path d="M0 0H6L10 5.5 6 11H0Z" fill="#fff"/></svg>CREATE BETTER RESULTS THROUGH BECOMING A GREATER THINKER</li>
    <li><svg width="10" height="11" viewBox="0 0 10 11"><path d="M0 0H6L10 5.5 6 11H0Z" fill="#fff"/></svg>MORE CHOICES ABOUT YOUR BEHAVIOURS AND EMOTIONS</li>
    <li><svg width="10" height="11" viewBox="0 0 10 11"><path d="M0 0H6L10 5.5 6 11H0Z" fill="#fff"/></svg>IMPROVE YOUR RELATIONSHIPS AND THE WAYS YOU COMMUNICATE</li>
    <li><svg width="10" height="11" viewBox="0 0 10 11"><path d="M0 0H6L10 5.5 6 11H0Z" fill="#fff"/></svg>CREATE BETTER RESULTS THROUGH BECOMING A GREATER THINKER</li>
    <li><svg width="10" height="11" viewBox="0 0 10 11"><path d="M0 0H6L10 5.5 6 11H0Z" fill="#fff"/></svg>MORE CHOICES ABOUT YOUR BEHAVIOURS AND EMOTIONS</li>
    <li><svg width="10" height="11" viewBox="0 0 10 11"><path d="M0 0H6L10 5.5 6 11H0Z" fill="#fff"/></svg>IMPROVE YOUR RELATIONSHIPS AND THE WAYS YOU COMMUNICATE</li>
    <li><svg width="10" height="11" viewBox="0 0 10 11"><path d="M0 0H6L10 5.5 6 11H0Z" fill="#fff"/></svg>CREATE BETTER RESULTS THROUGH BECOMING A GREATER THINKER</li>
  </ul>
</section>

<section class="video">
  <h2 class="abs section-title" style="left:568px;top:569px">WHAT DO YOU DO</h2>
  <div class="abs laptop-screen">
    <div class="display">
      <svg width="60" height="60" viewBox="0 0 60 60" aria-label="Play video"><circle cx="30" cy="30" r="29" fill="#000"/><path d="M23 17L44 30 23 43Z" fill="#fff"/></svg>
    </div>
  </div>
  <div class="abs laptop-base"></div>
</section>

<div class="abs rule" style="top:763px"></div>

<section class="featured">
  <h2 class="abs section-title" style="left:362px;top:774px">FEATURED CONTENT</h2>
  <div class="photo" style="left:107px;top:808px;width:294px;height:197px;background:linear-gradient(180deg,#4f8fd0 0%,#bcd7ee 45%,#7f9a55 70%,#d9c9a4 100%)" role="img" aria-label="Friends walking through beach dunes"></div>
  <div class="photo" style="left:410px;top:808px;width:164px;height:112px;background:linear-gradient(135deg,#9cc3dc,#3f6f9c)" role="img" aria-label="Woman using a tablet"></div>
  <div class="photo" style="left:582px;top:808px;width:164px;height:112px;background:linear-gradient(135deg,#f2ece6,#d9a15a 70%,#e58c3a)" role="img" aria-label="Fitness class doing push-ups"></div>
  <div class="photo" style="left:408px;top:925px;width:166px;height:78px;background:linear-gradient(90deg,#e8e2df,#e07a3c 50%,#f1d4c2)" role="img" aria-label="Smiling woman in a city street"></div>
  <div class="photo" style="left:580px;top:925px;width:166px;height:78px;background:linear-gradient(90deg,#f3efe8,#c98c62 50%,#b8333a)" role="img" aria-label="Group of friends together"></div>
  <div class="photo" style="left:107px;top:1010px;width:129px;height:74px;background:linear-gradient(135deg,#f3e9e2,#d8a88e)" role="img" aria-label="Holding hands"></div>
  <div class="photo" style="left:241px;top:1010px;width:202px;height:74px;background:linear-gradient(135deg,#e7a34a,#f0c58a 60%,#d98f6a)" role="img" aria-label="Relaxing on the beach"></div>
  <div class="photo" style="left:447px;top:1010px;width:299px;height:74px;background:linear-gradient(90deg,#1f3a5c,#5d87ad 50%,#2b4566)" role="img" aria-label="Two women laughing together"></div>
</section>

<footer>
  <div class="abs footer"></div>
  <div class="abs call">
    <svg width="32" height="32" viewBox="0 0 32 32" aria-label="Phone"><circle cx="16" cy="16" r="14.5" fill="none" stroke="#fff" stroke-width="2"/><path d="M11 9c1-1 2-1 2.5 0l1.5 3c.3.7 0 1.3-.6 1.8l-1 .8c.8 1.8 2.2 3.3 4 4.2l.8-1c.5-.6 1.1-.9 1.8-.6l3 1.5c1 .5 1 1.5 0 2.5-1.3 1.3-3 1.6-5 .6-3-1.6-5.4-4-7-7-1-2-.7-3.7.6-5z" fill="#fff"/></svg>
    CALL US: +61 02 5550 1427
  </div>
  <p class="abs follow">follow us:</p>
  <span class="abs social" style="left:632px" aria-label="Social link"></span>
  <span class="abs social" style="left:674px" aria-label="Social link"></span>
  <nav class="footer-nav">
    <a style="left:178px">HOME</a>
    <a style="left:225px">BUSINESS</a>
    <a style="left:287px">INDIVIDUAL</a>
    <a style="left:356px">CONTACT</a>
  </nav>
  <p class="abs copyright">COPYRIGHT@TIDES OF BLOOM</p>
  <div class="abs brand" style="left:627px;top:1160px;font-size:13px;gap:6px"><span class="brand-mark" style="width:22px;height:22px"></span>Tides of Bloom</div>
</footer>

</body>
</html>
```